Lawn Sign Design – Brisko

We need a clean, eye-catching 18" x 24" lawn sign for Brisko that effectively communicates our core message while maintaining strong brand consistency.

Key Elements to Include:
Tagline (Main Focus): Upgrade Your Roof Without Replacing It
Website: www.tryvexlo-demo.example
Phone Number: (877) BRISKO-GO
RQMH License Number: 4830516
Brisko Logo & Branding: Ensure the logo, corporate colors, and custom font are used consistently to align with our existing branding.

Design Guidelines:
Simple & High-Impact: The tagline should be the most prominent element on the sign, drawing immediate attention.
Easy Readability: Use a bold, clean design with high contrast for quick readability from a distance.
Balanced Layout: Place supporting details (website, phone number, and RQMH number) in a visually clear but secondary position to the tagline.
Professional & Modern: The sign should reflect credibility and innovation in the roofing industry.

Deliverables:
High-resolution print-ready files (CMYK)
A digital proof for review before finalizing
The final design should make a strong impression with minimal text, ensuring that anyone passing by can instantly grasp what we offer.

I am including our custom font. To get an hexagon in our name, simply type the $ after the 'O" Please use this font for anything you type.

```html
<!DOCTYPE html>
<html lang="en">
<head>
<meta charset="utf-8">
<title>Brisko Lawn Sign</title>
<link rel="stylesheet" href="https://fonts.googleapis.com/css2?family=Anton&family=Poppins:wght@500;600&display=swap">
<style>
  :root {
    --brand-charcoal: #2b2f33;
    --brand-blue: #1f5096;
    --brand-blue-deep: #184483;
    --brand-blue-light: #3465ab;
    --contact-blue: #0d4a9c;
    --white: #ffffff;
    --ink: #2b2f33;
  }
  html, body {
    margin: 0;
    padding: 0;
    width: 900px;
    height: 1200px;
    overflow: hidden;
    background: var(--white);
  }
  .lawn-sign {
    position: relative;
    width: 900px;
    height: 1200px;
    overflow: hidden;
  }
  .brand-band {
    position: absolute;
    left: 0;
    top: 0;
    width: 285px;
    height: 1200px;
    background: var(--brand-charcoal);
  }
  .hero-photo {
    position: absolute;
    left: 285px;
    top: 0;
    width: 615px;
    height: 1005px;
    background: linear-gradient(155deg, var(--brand-blue-deep) 0%, var(--brand-blue) 45%, var(--brand-blue-light) 70%, var(--brand-blue) 100%);
  }
  .contact-band {
    position: absolute;
    left: 285px;
    top: 1005px;
    width: 615px;
    height: 195px;
    background: var(--white);
  }
  .sign-art {
    position: absolute;
    left: 0;
    top: 0;
  }
  .brand-name {
    font-family: "Poppins", sans-serif;
    font-weight: 600;
    fill: var(--white);
  }
  .logo-mark { fill: var(--white); }
  .logo-name {
    font-family: "Poppins", sans-serif;
    font-weight: 600;
    fill: var(--white);
  }
  .tagline {
    font-family: "Anton", sans-serif;
    fill: var(--white);
  }
  .phone {
    font-family: "Poppins", sans-serif;
    font-weight: 600;
    fill: var(--contact-blue);
  }
  .website {
    font-family: "Poppins", sans-serif;
    font-weight: 500;
    fill: var(--ink);
  }
  .license {
    font-family: "Poppins", sans-serif;
    font-weight: 500;
    fill: var(--ink);
  }
</style>
</head>
<body>
  <main class="lawn-sign">
    <div class="brand-band"></div>
    <div class="hero-photo" role="img" aria-label="Photo of a roofer in a hard hat and plaid shirt standing by a tiled roof, tinted brand blue"></div>
    <div class="contact-band"></div>

    <svg class="sign-art" width="900" height="1200" viewBox="0 0 900 1200" xmlns="http://www.w3.org/2000/svg">
      <text class="brand-name" transform="translate(238 1154) rotate(-90)" x="0" y="0" font-size="262" textLength="1106" lengthAdjust="spacing">BRISKO</text>

      <g class="brand-lockup">
        <rect class="logo-mark" x="466" y="190" width="56" height="56"/>
        <text class="logo-name" x="540" y="240" font-size="66" textLength="181" lengthAdjust="spacingAndGlyphs">BRISKO</text>
      </g>

      <g class="tagline">
        <text x="327" y="580" font-size="115" textLength="504" lengthAdjust="spacingAndGlyphs">UPGRADE</text>
        <text x="327" y="691" font-size="115" textLength="287" lengthAdjust="spacingAndGlyphs">YOUR</text>
        <text x="327" y="805" font-size="115" textLength="287" lengthAdjust="spacingAndGlyphs">ROOF</text>
        <text x="327" y="893" font-size="83" textLength="328" lengthAdjust="spacingAndGlyphs">WITHOUT</text>
        <text x="327" y="970" font-size="76" textLength="477" lengthAdjust="spacingAndGlyphs">REPLACING IT</text>
      </g>

      <text class="phone" x="328" y="1103" font-size="60" textLength="521" lengthAdjust="spacingAndGlyphs">(877) BRISKO-GO</text>
      <text class="website" x="330" y="1146" font-size="30" textLength="524" lengthAdjust="spacingAndGlyphs">www.tryvexlo-demo.example</text>
      <text class="license" x="330" y="1182" font-size="17" textLength="150" lengthAdjust="spacingAndGlyphs">RQMH #4830516</text>
    </svg>
  </main>
</body>
</html>
```